Brand Identity Stationary Package

Hello I'm looking for a full branding package for my Property Management Company. I have a logo but looking to have the following
Business Card
Email signature
Facebook cover photo
Letterhead (word.doc)
#10 Envelope
Pocket Folder - link to 9x12 pocket folder design specs https://www.plorafine.ca/marketing-materials/presentation-folders
would like everything to match and be brand identifiable. The company looks after residential properties/apartments and some commercial properties. Attached is a zip of the files.
For Business Card
Name: Gideon Falkner
Position: Operations Manager
Number: 1 (506) 384-2917
Email: Gideon@quarrytide.ca
Website: Quarrytide.ca
Property Management

```html
<!DOCTYPE html>
<html lang="en">
<head>
<meta charset="utf-8">
<title>Quarrytide Property Management – Stationery</title>
<link rel="stylesheet" href="https://fonts.googleapis.com/css2?family=Montserrat:wght@400;600&family=Roboto:wght@300&display=swap">
<style>
  :root{
    --backdrop:#a8a9ad;
    --paper:#ffffff;
    --ink:#231f20;
    --green:#7aae3d;
    --muted:#3a3a3a;
    --ghost:#e6e7e8;
    --rule:#bdbdbd;
  }
  *{box-sizing:border-box;margin:0;padding:0}
  html,body{width:1200px;height:857px;overflow:hidden}
  body{background:var(--backdrop);position:relative;font-family:"Montserrat",sans-serif;color:var(--ink)}
  .sheet{position:absolute;background:var(--paper);overflow:hidden}
  .sheet--dark{background:var(--ink)}

  .brand{position:absolute;display:flex;flex-direction:column;align-items:flex-start;line-height:1}
  .brand--center{align-items:center}
  .brand__name{font-family:"Montserrat",sans-serif;font-weight:600;letter-spacing:.06em;color:var(--ink)}
  .brand__tag{font-family:"Montserrat",sans-serif;font-weight:600;letter-spacing:.62em;color:var(--ink);margin-top:.35em}
  .brand--light .brand__name,.brand--light .brand__tag{color:#fff}

  .contact{position:absolute;font-family:"Montserrat",sans-serif;color:var(--muted);list-style:none}
  .contact li{display:flex;align-items:center;white-space:nowrap}
  .contact svg{fill:var(--green);margin-right:.45em;flex:none}

  .ghost-block{position:absolute;background:linear-gradient(160deg,#ececed,var(--ghost))}

  /* letterhead */
  .letterhead{left:274px;top:146px;width:400px;height:565px}
  .letter{position:absolute;left:43px;top:133px;width:314px;font-family:"Roboto",sans-serif;font-weight:300;font-size:6.6px;line-height:9.4px;color:var(--ink)}
  .letter p{margin-bottom:9.4px}
  .letter .body{text-align:justify}
  .signature{display:block;width:92px;height:14px;margin-top:3px;background:linear-gradient(90deg,#e9e9ea,#f4f4f4);border-radius:2px}

  /* email signature */
  .email-sig{left:699px;top:186px;width:302px;height:93px}
  .email-sig__rule{position:absolute;left:164px;top:20px;width:1px;height:53px;background:var(--rule)}
  .person__name{font-family:"Montserrat",sans-serif;font-weight:600;color:var(--green)}
  .person__role{font-family:"Montserrat",sans-serif;color:var(--muted)}
  .social{position:absolute;left:65px;top:56px;display:flex;gap:4px}
  .social span{width:9px;height:9px;border-radius:50%;background:var(--green)}

  .envelope-front{left:699px;top:304px;width:439px;height:191px}
  .envelope-back{left:699px;top:520px;width:439px;height:191px}
  .card-front{left:62px;top:472px;width:187px;height:107px}
  .card-back{left:62px;top:605px;width:187px;height:107px}
  .card-back__url{position:absolute;left:19px;top:89px;font-size:4.4px;color:#fff}
  .card-front__rule{position:absolute;left:93px;top:63px;width:.6px;height:16px;background:var(--rule)}
</style>
</head>
<body>
<svg width="0" height="0" style="position:absolute">
  <symbol id="icon-phone" viewBox="0 0 10 10"><path d="M2 1l2 2-1 1.2c.6 1.2 1.5 2.1 2.8 2.8L7 6l2 2-1.3 1.3C4.5 9 1 5.5.7 2.3z"/></symbol>
  <symbol id="icon-mail" viewBox="0 0 10 10"><path d="M1 2.5h8v5H1zM1.8 3.2v3.6h6.4V3.2L5 5.4z" fill-rule="evenodd"/></symbol>
  <symbol id="icon-web" viewBox="0 0 10 10"><circle cx="5" cy="5" r="4"/></symbol>
</svg>

<!-- Letterhead -->
<section class="sheet letterhead">
  <div class="brand brand--center" style="left:0;width:400px;top:27px">
    <span class="brand__name" style="font-size:18px">QUARRYTIDE</span>
    <span class="brand__tag" style="font-size:5px">PROPERTY MANAGEMENT</span>
  </div>
  <div class="letter">
    <p>01 January 2050</p>
    <p>Company (Pvt) Ltd.<br>PO Box 3355 Mainville St<br>Sample City Country 3355</p>
    <p style="margin-top:18px">Dear Alden Marsh,</p>
    <p class="body">Lorem ipsum dolor sit amet, consectetuer adipiscing elit, sed diam nonummy nibh euismod tincidunt ut laoreet dolore magna aliquam erat volutpat. Ut wisi enim ad minim veniam, quis nostrud exerci tation ullamcorper suscipit lobortis nisl ut aliquip ex ea commodo consequat. Duis dolore te feugait nulla facilisi. Nam liber tempor cum soluta nobis eleifend option congue nihil imperdiet doming id quod mazim placerat facer possim assum. Lorem ipsum dolor sit amet, consectetuer adipiscing elit, sed diam nonummy nibh euismod tincidunt ut laoreet dolore magna aliquam erat volutpat. Ut wisi enim ad minim veniam, quis nostrud exerci tation ullamcorper suscipit lobortis nisl ut aliquip ex ea commodo consequat.</p>
    <p class="body">Consectetuer adipiscing elit, sed diam nonummy nibh euismod tincidunt ut laoreet dolore magna aliquam erat volutpat. Ut wisi enim ad minim veniam, quis nostrud exerci tation ullamcorper suscipit lobortis nisl ut aliquip ex ea commodo consequat. Consectetuer adipiscing elit, sed diam nonummy nibh euismod tincidunt ut laoreet dolore magna aliquam erat volutpat. Ut wisi enim ad minim veniam, quis nostrud exerci tation ullamcorper suscipit lobortis nisl ut aliquip ex ea commodo consequat.</p>
    <p class="body">Consectetuer adipiscing elit, sed diam nonummy nibh euismod tincidunt ut laoreet dolore magna aliquam erat volutpat. Ut wisi enim ad minim veniam, quis nostrud exerci tation ullamcorper suscipit lobortis nisl ut aliquip ex ea commodo consequat. Consectetuer adipiscing elit, sed diam nonummy nibh euismod tincidunt ut laoreet dolore magna aliquam erat volutpat. Ut wisi enim ad minim veniam, quis nostrud exerci tation ullamcorper suscipit lobortis nisl ut aliquip ex ea commodo consequat.</p>
    <p style="margin-top:24px;margin-bottom:0">Sincerely Yours</p>
    <span class="signature" role="img" aria-label="Handwritten signature of Rowan Castell"></span>
  </div>
  <div class="ghost-block" style="left:202px;top:434px;width:198px;height:131px" role="img" aria-label="Faint large brand symbol watermark"></div>
  <ul class="contact" style="left:34px;top:524px;font-size:6.6px;line-height:8.2px">
    <li><svg width="5" height="5"><use href="#icon-phone"/></svg>1 (506) 384-2917</li>
    <li><svg width="5" height="5"><use href="#icon-mail"/></svg>Gideon@quarrytide.ca</li>
    <li><svg width="5" height="5"><use href="#icon-web"/></svg>www.Quarrytide.ca</li>
  </ul>
</section>

<!-- Email signature -->
<section class="sheet email-sig">
  <div class="brand" style="left:27px;top:27px">
    <span class="brand__name" style="font-size:15px">QUARRYTIDE</span>
    <span class="brand__tag" style="font-size:4.4px">PROPERTY MANAGEMENT</span>
  </div>
  <div class="social"><span></span><span></span><span></span><span></span></div>
  <div class="email-sig__rule"></div>
  <div style="position:absolute;left:177px;top:19px">
    <div class="person__name" style="font-size:9.4px">Gideon Falkner</div>
    <div class="person__role" style="font-size:7.4px;margin-top:1px">Operations Manager</div>
  </div>
  <ul class="contact" style="left:177px;top:47px;font-size:7.4px;line-height:9px">
    <li><svg width="5" height="5"><use href="#icon-phone"/></svg>1 (506) 384-2917</li>
    <li><svg width="5" height="5"><use href="#icon-mail"/></svg>Gideon@quarrytide.ca</li>
    <li><svg width="5" height="5"><use href="#icon-web"/></svg>www.Quarrytide.ca</li>
  </ul>
</section>

<!-- Envelope front -->
<section class="sheet envelope-front">
  <div class="brand" style="left:34px;top:29px">
    <span class="brand__name" style="font-size:17px">QUARRYTIDE</span>
    <span class="brand__tag" style="font-size:4.9px">PROPERTY MANAGEMENT</span>
  </div>
  <div class="ghost-block" style="left:251px;top:64px;width:188px;height:127px" role="img" aria-label="Faint large brand symbol watermark"></div>
  <ul class="contact" style="left:34px;top:138px;font-size:6.4px;line-height:8px">
    <li><svg width="5" height="5"><use href="#icon-phone"/></svg>1 (506) 384-2917</li>
    <li><svg width="5" height="5"><use href="#icon-mail"/></svg>Gideon@quarrytide.ca</li>
    <li><svg width="5" height="5"><use href="#icon-web"/></svg>www.Quarrytide.ca</li>
  </ul>
</section>

<!-- Envelope back -->
<section class="sheet envelope-back">
  <svg width="439" height="191" style="position:absolute;left:0;top:0">
    <path d="M13 62 Q14 68 22 68 L417 68 Q424 68 426 62 L439 0 L0 0 Z" fill="var(--ink)"/>
    <path d="M14 66 L8 185 M425 66 L431 185" stroke="#e2e2e2" stroke-width=".6" fill="none"/>
  </svg>
  <div class="brand brand--center brand--light" style="left:0;width:439px;top:20px">
    <span class="brand__name" style="font-size:15px">QUARRYTIDE</span>
    <span class="brand__tag" style="font-size:4.4px">PROPERTY MANAGEMENT</span>
  </div>
</section>

<!-- Business card front -->
<section class="sheet card-front">
  <div class="brand brand--center" style="left:0;width:187px;top:24px">
    <span class="brand__name" style="font-size:11px">QUARRYTIDE</span>
    <span class="brand__tag" style="font-size:3.2px">PROPERTY MANAGEMENT</span>
  </div>
  <div style="position:absolute;right:98px;top:64px;text-align:center">
    <div class="person__name" style="font-size:5.6px">Gideon Falkner</div>
    <div class="person__role" style="font-size:4.2px">Operations Manager</div>
  </div>
  <div class="card-front__rule"></div>
  <ul class="contact" style="left:102px;top:63px;font-size:4.2px;line-height:5.6px">
    <li><svg width="3" height="3"><use href="#icon-phone"/></svg>1 (506) 384-2917</li>
    <li><svg width="3" height="3"><use href="#icon-mail"/></svg>Gideon@quarrytide.ca</li>
    <li><svg width="3" height="3"><use href="#icon-web"/></svg>www.Quarrytide.ca</li>
  </ul>
</section>

<!-- Business card back -->
<section class="sheet sheet--dark card-back">
  <div class="brand brand--light" style="left:19px;top:19px">
    <span class="brand__name" style="font-size:14px">QUARRYTIDE</span>
    <span class="brand__tag" style="font-size:4.1px">PROPERTY MANAGEMENT</span>
  </div>
  <div style="position:absolute;left:90px;top:41px;width:97px;height:66px;background:linear-gradient(160deg,#86b24a,var(--green))" role="img" aria-label="Large green brand symbol graphic"></div>
  <span class="card-back__url">www.Quarrytide.ca</span>
</section>
</body>
</html>
```